MossVane Spa, Skincare and Cosmetics website

I need a website for MossVane (putting the glow back into people's skin) which allows viewers to access information about Beauty Spa packaging and facilities as well as online skincare and cosmetic products. Our distinctive difference is that our products are certified organic. We want to target a luxury high income niche market (age 30-50). I want all colours to be "baby colours" preferably background to be "baby metallic pink" (but please don't make the website too immature) with curves as patterns. I want a romantic vintage look.

The website needs to look:
1. elegant (prestige and luxury)
2. bright (baby colours mainly)
3. European curves and signature patterns
4. Can include Pearl related pics (but not a must)

The website pages needs to have:
1. pages ordering skincare/cosmetics
2. shopping cart and payment
3. about us and about our product differences
4. contact us
5. booking for spa treatments and packages

I have attached our logo and also packaging label styles.

Industry/Entity Type

Cosmetics

```html
<!DOCTYPE html>
<html lang="en">
<head>
<meta charset="utf-8">
<title>MossVane Spa, Skincare and Cosmetics</title>
<link rel="stylesheet" href="https://fonts.googleapis.com/css2?family=Cinzel:wght@400&family=Open+Sans:wght@400;600&family=Open+Sans+Condensed:wght@300&display=swap">
<style>
  :root {
    --page-pink: #f282b8;
    --page-pink-light: #f59bc6;
    --panel: #ffffff;
    --rose: #e2639c;
    --rose-deep: #d2528c;
    --rose-dark: #c23d7c;
    --booking: #ee7fb4;
    --ink: #2b2b2b;
    --body: #555555;
    --muted: #8f8f8f;
    --accent: #e3649c;
    --input-border: #d9d9d9;
  }
  * { box-sizing: border-box; margin: 0; padding: 0; }
  html, body { width: 1000px; height: 1200px; overflow: hidden; }
  body {
    position: relative;
    background: radial-gradient(circle at 50% 40%, var(--page-pink-light), var(--page-pink));
    font-family: "Open Sans", sans-serif;
    color: var(--body);
  }
  .panel {
    position: absolute; left: 88px; top: 27px; width: 833px; height: 1064px;
    background: var(--panel); border-radius: 4px;
    box-shadow: 0 0 0 6px rgba(255,255,255,0.18);
  }
  .social { position: absolute; left: 766px; top: 39px; display: flex; gap: 3px; }
  .social span { width: 25px; height: 25px; border-radius: 50%; background: #f4a3c8; display: block; }

  .nav-band {
    position: absolute; left: 98px; top: 77px; width: 806px; height: 49px;
    background: var(--rose); border-radius: 10px;
    border: 1px dashed rgba(255,255,255,0.6); outline: 3px solid var(--rose); outline-offset: -5px;
    box-shadow: 0 2px 3px rgba(0,0,0,0.15);
  }
  .nav { position: absolute; top: 94px; display: flex; gap: 27px; font-size: 13.5px; color: #fff; }
  .nav-left { left: 129px; }
  .nav-right { left: 601px; }

  .badge { position: absolute; left: 407px; top: 43px; width: 184px; height: 126px; }
  .badge-name {
    position: absolute; left: 407px; top: 118px; width: 184px; text-align: center;
    font-family: "Cinzel", serif; font-size: 22px; color: #fff; letter-spacing: 1px;
  }
  .badge-dot {
    position: absolute; left: 484px; top: 62px; width: 32px; height: 32px;
    border-radius: 50%; background: #f3b6d1;
  }

  .hero {
    position: absolute; left: 106px; top: 126px; width: 790px; height: 328px;
    background: linear-gradient(100deg, #cfb79b 0%, #e8d3c0 30%, #f0c9b4 50%, #ecdccd 72%, #f6eef0 100%);
    border-radius: 0 0 8px 8px; box-shadow: 0 0 0 4px #fff, 0 0 0 5px #eee;
  }
  .hero-dots { position: absolute; left: 476px; top: 436px; display: flex; gap: 3px; }
  .hero-dots span { width: 11px; height: 11px; border-radius: 50%; background: #fff; display: block; }

  .welcome-title {
    position: absolute; left: 108px; top: 491px; font-family: "Cinzel", serif;
    font-size: 23px; color: var(--ink); font-weight: 400;
  }
  .welcome-text { position: absolute; left: 109px; top: 525px; width: 520px; font-size: 10.2px; line-height: 18px; }
  .welcome-text p + p { margin-top: 8px; }

  .section-title {
    position: absolute; font-family: "Cinzel", serif; font-size: 21px; font-weight: 400;
  }
  .treat-title { left: 108px; top: 686px; color: var(--accent); }

  .treatment { position: absolute; width: 167px; }
  .treatment .photo { height: 90px; border-radius: 3px; }
  .treatment h3 { font-weight: 400; font-size: 14px; color: #444; margin: 6px 0 0 3px; }
  .treatment p { font-size: 10px; line-height: 16px; color: var(--muted); margin: 2px 0 0 3px; }

  .booking {
    position: absolute; left: 655px; top: 486px; width: 241px; height: 243px;
    background: var(--booking); border-radius: 7px; overflow: hidden;
    box-shadow: 0 0 0 2px var(--rose);
  }
  .booking::after {
    content: ""; position: absolute; inset: 3px; border: 1px dashed rgba(255,255,255,0.7); border-radius: 5px;
  }
  .booking-head {
    height: 47px; background: var(--rose-deep); color: #fff; font-family: "Cinzel", serif;
    font-size: 18px; padding: 14px 0 0 19px;
  }
  .booking-field {
    position: absolute; left: 18px; width: 203px; height: 24px; background: #fff;
    border: 1px solid var(--input-border); border-radius: 3px; font-size: 10px; color: #777;
    padding: 5px 0 0 9px;
  }
  .booking-btn {
    position: absolute; left: 113px; top: 196px; width: 108px; height: 29px;
    background: var(--rose-dark); color: #fff; font-size: 13px; text-align: center; padding-top: 6px;
    border-radius: 3px; box-shadow: 0 0 0 1px #fff;
  }

  .blog-title { left: 656px; top: 752px; color: #555; }
  .post { position: absolute; left: 656px; width: 240px; height: 70px; }
  .post .thumb {
    position: absolute; left: 0; top: 0; width: 74px; height: 70px; border-radius: 2px;
    box-shadow: 0 0 0 4px #fff, 0 0 0 5px #e5e5e5;
  }
  .post h4 { position: absolute; left: 83px; top: -3px; font-weight: 400; font-size: 12px; color: var(--accent); }
  .post p { position: absolute; left: 83px; top: 14px; width: 160px; font-size: 9.3px; line-height: 16.5px; color: #444; }

  .footer-nav {
    position: absolute; left: 0; top: 1119px; width: 1000px; text-align: center;
    font-family: "Open Sans Condensed", "Open Sans", sans-serif; font-size: 15px; color: #fff;
    word-spacing: 2px;
  }
  .copyright { position: absolute; left: 0; top: 1148px; width: 1000px; text-align: center; font-size: 10px; color: #fce3ef; }
</style>
</head>
<body>
  <div class="panel"></div>

  <div class="social" aria-label="Social links">
    <span></span><span></span><span></span><span></span>
  </div>

  <div class="nav-band"></div>
  <nav class="nav nav-left"><span>HOME</span><span>ABOUT</span><span>TREATMENT</span><span>SPA</span></nav>
  <nav class="nav nav-right"><span>PRODUCT</span><span>TESTIMONIALS</span><span>CONTACT</span></nav>

  <svg class="badge" viewBox="0 0 184 126" aria-hidden="true">
    <path d="M18 6 Q92 20 166 6 Q182 6 178 24 Q172 62 180 96 Q184 110 166 108 Q120 106 96 124 Q92 127 88 124 Q64 106 18 108 Q0 110 4 96 Q12 62 6 24 Q2 6 18 6 Z"
          fill="#e2639c" stroke="#d2528c" stroke-width="2"/>
    <path d="M20 12 Q92 26 164 12 Q175 12 172 26 Q166 62 174 94 Q176 103 164 102 Q118 100 92 117 Q66 100 20 102 Q8 103 10 94 Q18 62 12 26 Q9 12 20 12 Z"
          fill="none" stroke="#fff" stroke-opacity="0.7" stroke-dasharray="3 2"/>
  </svg>
  <div class="badge-dot"></div>
  <div class="badge-name">MossVane</div>

  <div class="hero" role="img" aria-label="Photo of a relaxing facial massage with spa stones, herbal compresses and white orchids"></div>
  <div class="hero-dots"><span></span><span></span><span></span><span></span></div>

  <h1 class="welcome-title">WELCOME TO MOSSVANE HOMEPAGE</h1>
  <div class="welcome-text">
    <p>Mauris vel lacus vitae felis vestibulum volutpat Etiam est nunc venenatis in tristique eu imperdiet ac nisl Cum sociis natoque penatibus et magnis dis parturient montes nascetur ridiculus mus In iaculis facilisis massa Etiam eu urna Sed porta Suspendisse quam leo molestie sed luctus quis feugiat in pede Fusce tellus Sed metus augue convallis et vehicula ut pulvinar eu ante Integer orci tellus tristique vitae consequat nec porta vel lectus N</p>
    <p>Suspendisse vulputate aliquam dui Nulla elementum dui ut augue Aliquam vehicula mi at mauris Maecenas lacerat nisl at consequat rhoncus sem nunc gravida justo quis eleifend arcu velit quis lacus</p>
  </div>

  <h2 class="section-title treat-title">TREATMENT &amp; CARE</h2>

  <article class="treatment" style="left:109px;top:720px">
    <div class="photo" role="img" aria-label="Photo of a back massage with rose petals and candles" style="background:linear-gradient(135deg,#d9b9a6,#f2d4cc 55%,#e7a7b3)"></div>
    <h3>Donec scelerisque</h3><p>Nam cursus Morbi ut mi Nullam enim leo egestas id cond</p>
  </article>
  <article class="treatment" style="left:286px;top:720px">
    <div class="photo" role="img" aria-label="Photo of a facial mask treatment with towel wrap and lilies" style="background:linear-gradient(135deg,#f3e9df,#e9d2c4 50%,#d9c3b9)"></div>
    <h3>Vivamus metus</h3><p>Nam cursus Morbi ut mi Nullam enim leo egestas id cond</p>
  </article>
  <article class="treatment" style="left:462px;top:720px">
    <div class="photo" role="img" aria-label="Photo of aloe vera gel being applied to skin" style="background:linear-gradient(135deg,#f5efe9,#eedfd3 50%,#e8c9b3)"></div>
    <h3>Morbi ut mi</h3><p>Nam cursus Morbi ut mi Nullam enim leo egestas id cond</p>
  </article>
  <article class="treatment" style="left:109px;top:896px">
    <div class="photo" role="img" aria-label="Photo of a relaxing face massage" style="background:linear-gradient(135deg,#c99a78,#e8c3a5 50%,#f1e2d6)"></div>
    <h3>Phasellus felis</h3><p>Nam cursus Morbi ut mi Nullam enim leo egestas id cond</p>
  </article>
  <article class="treatment" style="left:286px;top:896px">
    <div class="photo" role="img" aria-label="Photo of fresh glowing skin among green leaves" style="background:linear-gradient(135deg,#d6e8a6,#f1e8d6 50%,#b9d88a)"></div>
    <h3>Tempus libero</h3><p>Nam cursus Morbi ut mi Nullam enim leo egestas id cond</p>
  </article>
  <article class="treatment" style="left:462px;top:896px">
    <div class="photo" role="img" aria-label="Photo of a clay face mask with flowers on a green towel" style="background:linear-gradient(135deg,#8fb35c,#e6d9cb 50%,#6e9c4a)"></div>
    <h3>Mauris neque metus</h3><p>Nam cursus Morbi ut mi Nullam enim leo egestas id cond</p>
  </article>

  <form class="booking">
    <div class="booking-head">QUICK BOOKING</div>
    <div class="booking-field" style="top:60px">Your Name</div>
    <div class="booking-field" style="top:93px">Email address</div>
    <div class="booking-field" style="top:125px">Phone no.</div>
    <div class="booking-field" style="top:158px">Booking Time</div>
    <div class="booking-btn">BOOK NOW</div>
  </form>

  <h2 class="section-title blog-title">RECENT BLOG POST</h2>
  <article class="post" style="top:791px">
    <div class="thumb" role="img" aria-label="Photo of smooth facial skin" style="background:linear-gradient(135deg,#f3d5cc,#e7b4aa)"></div>
    <h4>Phasellus felis dolor</h4>
    <p>Maecenas aliquet velit vel turpis. Mauris neque metus, malesuada nec, ultricies sit ame</p>
  </article>
  <article class="post" style="top:874px">
    <div class="thumb" role="img" aria-label="Photo of a woman in a towel wrap" style="background:linear-gradient(135deg,#f1f1f1,#e4c6b4)"></div>
    <h4>Phasellus felis dolor</h4>
    <p>Maecenas aliquet velit vel turpis. Mauris neque metus, malesuada nec, ultricies sit ame</p>
  </article>
  <article class="post" style="top:961px">
    <div class="thumb" role="img" aria-label="Photo of a facial massage" style="background:linear-gradient(135deg,#c99870,#ecd0b6)"></div>
    <h4>Phasellus felis dolor</h4>
    <p>Maecenas aliquet velit vel turpis. Mauris neque metus, malesuada nec, ultricies sit ame</p>
  </article>

  <nav class="footer-nav">HOME | ABOUT | TREATMENT | SPA | PRODUCT | TESTIMONIALS | CONTACT</nav>
  <p class="copyright">© 2013 Company Name. All right reserved. Term of Use</p>
</body>
</html>
```